Easy Business Card / Presentation Cover Design Project

We are looking for a business card design, covers for powerpoint presentations for investors, and possibly simple stationary for a Chicago real estate development firm. Our new logo is attached below.

We rehab and provide newly constructed homes. We are not a real estate brokerage firm (i.e., agents such as Meridale 47) and only operate in the Chicago area.

In terms of design, sophisticated and high end that would appeal to investors (theme should resemble investment banks, hedge funds, private equity rather than tech startup).

Target Market(s)

Investors, banks, financing sources

Industry/Entity Type

Real Estate

Requirements
Must have
• Two deliverables here. 1) Business card 2) Covers for powerpoint presentation.

Must be able to look sophisticated and high end when printed. Please think through the type of printing that will be needed. Would prefer something that can be printed in raised ink but digital is ok as well.

Will be printed on heavy paper.

Business Card: Horizontal Layout, no black backgrounds,

For presentation front cover, should include logo only. For back cover, should include contact info. Horizontal and should not contain any information that will need to be changed (i.e. date or client name)
Nice to have
• Would like to have the edges colored but not required. Please show multiple designs
Should not have
• Should not have any die cut or embossed type of designs. Shape should be standard size.

We are not a design firm, a retail firm, or a consumer product firm.

Please do not incorporate a house, buildings, etc. This must be very professional looking.

```html
<!DOCTYPE html>
<html lang="en">
<head>
<meta charset="utf-8">
<title>Orvane Realty – Presentation Cover</title>
<link rel="stylesheet" href="https://fonts.googleapis.com/css2?family=Open+Sans:wght@400;600;700&display=swap">
<style>
  :root {
    --paper: #ffffff;
    --brand-blue: #1565d8;
    --ring-blue: #1e90f0;
    --mist-blue: #e6f3fd;
    --mist-deep: #cfe6fa;
    --ink-grey: #5a5a5a;
    --mark-grey: #6b6b6b;
  }
  html, body {
    margin: 0;
    padding: 0;
    width: 1200px;
    height: 900px;
    overflow: hidden;
    background: var(--paper);
  }
  .cover {
    position: relative;
    width: 1200px;
    height: 900px;
    background: var(--paper);
    font-family: "Open Sans", Arial, sans-serif;
    overflow: hidden;
  }
  .client-block {
    position: absolute;
    left: 62px;
    top: 320px;
  }
  .client-name {
    margin: 0 0 28px;
    font-size: 51px;
    font-weight: 700;
    letter-spacing: 0.5px;
    color: var(--brand-blue);
    line-height: 1.1;
  }
  .client-address,
  .client-contact {
    margin: 0;
    font-size: 24px;
    line-height: 36px;
    color: var(--ink-grey);
    font-weight: 400;
  }
  .client-address { margin-bottom: 16px; }
  .client-address span,
  .client-contact span { display: block; }
  .brand-emblem {
    position: absolute;
    left: 0;
    top: 0;
  }
  .brand-name {
    font-family: "Open Sans", Arial, sans-serif;
    font-weight: 600;
    fill: var(--mark-grey);
  }
</style>
</head>
<body>
  <main class="cover">
    <svg class="brand-emblem" width="1200" height="900" viewBox="0 0 1200 900" aria-hidden="false">
      <defs>
        <radialGradient id="mist" cx="0.55" cy="0.5" r="0.6">
          <stop offset="0" stop-color="var(--mist-deep)"/>
          <stop offset="1" stop-color="var(--mist-blue)"/>
        </radialGradient>
      </defs>
      <ellipse cx="1022" cy="370" rx="228" ry="203" fill="var(--ring-blue)"/>
      <ellipse cx="1040" cy="370" rx="214" ry="196" fill="url(#mist)"
               role="img" aria-label="Soft swirling blue background texture"/>
      <circle cx="912" cy="368" r="50" fill="none" stroke="var(--mark-grey)" stroke-width="6"/>
      <text class="brand-name" x="982" y="362" font-size="44">Orvane</text>
      <text class="brand-name" x="982" y="410" font-size="44">Realty</text>
    </svg>

    <section class="client-block">
      <h1 class="client-name">COMPANY CLIENT NAME</h1>
      <p class="client-address">
        <span>Company Address 1</span>
        <span>Company Address 2</span>
      </p>
      <p class="client-contact">
        <span>Phone : 00 00 0121</span>
        <span>Telefax : 00 00 0121</span>
      </p>
    </section>
  </main>
</body>
</html>
```